Global E-commerce Business Needs Banner Ad

We need banner ads for a fast growing E-commerce business cater mostly to women. The ads must have unique and beautiful background that accentuate the products. The ads should also have between 1-4 products in it. It needs to have the headline "Up To 80% Off Retail" in the ad. The ad also needs to have our logo and a "View Now" button. The ad should be more feminine and playful. Each product should have a different background design specially for the product to make it more beautiful.

Dimension: 320 by 480 pixel

Target Market(s)

Women

Industry/Entity Type

Business

Requirements
Must have
• 1) "Up To 80% Off Retail"
• 2) Brimvale Logo
• 3) "View Now" button

```html
<!DOCTYPE html>
<html lang="en">
<head>
<meta charset="utf-8">
<title>Brimvale Banner Ads</title>
<link rel="stylesheet" href="https://fonts.googleapis.com/css2?family=Lora:ital,wght@0,400;1,400&family=Pinyon+Script&display=swap">
<style>
  :root {
    --stage-light: #d4d4d4;
    --stage-dark: #8f8f8f;
    --banner-black: #050505;
    --banner-soft: #1c1c1c;
    --header-white: #fbfbfb;
    --ink-dark: #1a1a1a;
    --text-light: #f1f1f1;
    --button-line: #d8d8d8;
  }
  * { margin: 0; padding: 0; box-sizing: border-box; }
  html, body { width: 1200px; height: 900px; overflow: hidden; }
  body {
    position: relative;
    background: radial-gradient(ellipse 75% 70% at 50% 40%, var(--stage-light) 0%, #c0c0c0 55%, var(--stage-dark) 100%);
  }
  .banner {
    position: absolute;
    top: 171px;
    width: 320px;
    height: 480px;
    background: radial-gradient(ellipse 80% 60% at 50% 45%, var(--banner-soft) 0%, var(--banner-black) 80%);
    overflow: hidden;
  }
  .banner--one { left: 77px; }
  .banner--two { left: 444px; }
  .banner--three { left: 810px; }
  .banner-header {
    position: absolute;
    top: 0; left: 0;
    width: 320px; height: 61px;
  }
  .brand-name {
    position: absolute;
    top: 14px; left: 0; width: 100%;
    text-align: center;
    font-family: "Lora", Georgia, serif;
    font-weight: 400;
    font-size: 24px;
    letter-spacing: 0.5px;
    color: var(--ink-dark);
    text-transform: uppercase;
  }
  .headline {
    position: absolute;
    top: 78px; left: 0; width: 100%;
    text-align: center;
    font-family: "Lora", Georgia, serif;
    font-style: italic;
    font-weight: 400;
    font-size: 22px;
    color: var(--text-light);
  }
  .product-photo {
    position: absolute;
    top: 118px; left: 60px;
    width: 200px; height: 270px;
    border-radius: 14px;
    box-shadow: 0 18px 30px rgba(0,0,0,0.6);
  }
  .banner--one .product-photo {
    background: linear-gradient(160deg, #5c5c62 0%, #3a3a40 40%, #1f1f23 100%);
  }
  .banner--two .product-photo {
    background: linear-gradient(160deg, #e0c27a 0%, #b98f3e 45%, #5d4520 100%);
  }
  .banner--three .product-photo {
    background: linear-gradient(160deg, #c2407f 0%, #9c8fb2 45%, #5e5e6a 100%);
  }
  .view-now {
    position: absolute;
    top: 403px; left: 19px;
    width: 283px; height: 57px;
    border: 1px solid var(--button-line);
    display: flex; align-items: center; justify-content: center;
    font-family: "Pinyon Script", cursive;
    font-size: 38px;
    line-height: 1;
    color: var(--text-light);
    padding-right: 20px;
    text-decoration: none;
  }
</style>
</head>
<body>

<section class="banner banner--one">
  <svg class="banner-header" viewBox="0 0 320 61" aria-hidden="true"><polygon points="0,0 320,0 320,42 160,61 0,42" fill="var(--header-white)"/></svg>
  <div class="brand-name">Brimvale</div>
  <h2 class="headline">Up To 80% Off Retail</h2>
  <div class="product-photo" role="img" aria-label="Black metal rose ring with pink stone and matching diamond band"></div>
  <a class="view-now" href="#">View Now</a>
</section>

<section class="banner banner--two">
  <svg class="banner-header" viewBox="0 0 320 61" aria-hidden="true"><polygon points="0,0 320,0 320,42 160,61 0,42" fill="var(--header-white)"/></svg>
  <div class="brand-name">Brimvale</div>
  <h2 class="headline">Up To 80% Off Retail</h2>
  <div class="product-photo" role="img" aria-label="Gold ring with pavé diamonds and a large solitaire"></div>
  <a class="view-now" href="#">View Now</a>
</section>

<section class="banner banner--three">
  <svg class="banner-header" viewBox="0 0 320 61" aria-hidden="true"><polygon points="0,0 320,0 320,42 160,61 0,42" fill="var(--header-white)"/></svg>
  <div class="brand-name">Brimvale</div>
  <h2 class="headline">Up To 80% Off Retail</h2>
  <div class="product-photo" role="img" aria-label="Silver ring with pink centre stone flanked by blue stones"></div>
  <a class="view-now" href="#">View Now</a>
</section>

</body>
</html>
```